Letterhead for invoices and engagement letter

Want to use logos sourced on pixelbazaar to create letterhead templates for word or pdf files

Industry/Entity Type

Legal- law firm

Colors
0054AA
0677BA
7BADD7
CADEEF
E8F1F8

```html
<!DOCTYPE html>
<html lang="en">
<head>
<meta charset="utf-8">
<title>The Calder Firm PLC – Letterhead and Invoice</title>
<link rel="stylesheet" href="https://fonts.googleapis.com/css2?family=EB+Garamond:wght@400;600&family=Open+Sans:wght@400;600;700&display=swap">
<style>
  :root {
    --navy: #0a1f3b;
    --grey-band: #a3a3a3;
    --backdrop: #e3e3e3;
    --paper: #ffffff;
    --ink: #1d1d1d;
    --contact-ink: #222222;
    --rule: #c9c9c9;
    --sig-tone: #eef0f3;
  }
  * { box-sizing: border-box; margin: 0; padding: 0; }
  html, body { width: 1200px; height: 741px; overflow: hidden; }
  body { background: var(--backdrop); position: relative; font-family: "Open Sans", sans-serif; color: var(--ink); }

  .sheet { position: absolute; top: 61px; width: 477px; height: 618px; background: var(--paper); box-shadow: 0 2px 6px rgba(0,0,0,.18); }
  .sheet--letter { left: 132px; }
  .sheet--invoice { left: 633px; }

  .brand { position: absolute; left: 45px; top: 62px; }
  .brand__name { font-family: "Open Sans", sans-serif; font-weight: 600; color: var(--navy); font-size: 14px; line-height: 18px; white-space: nowrap; }

  .contact { position: absolute; right: 41px; font-family: "EB Garamond", serif; font-size: 8px; line-height: 10px; text-align: right; color: var(--contact-ink); }
  .contact p.gap { margin-top: 4px; }
  .sheet--letter .contact { top: 33px; }
  .sheet--invoice .contact { top: 48px; }
  .invoice-title { position: absolute; right: 54px; top: 29px; font-family: "EB Garamond", serif; font-weight: 600; font-size: 16px; line-height: 20px; letter-spacing: .5px; color: var(--navy); }

  .letter { position: absolute; left: 45px; width: 391px; font-size: 8px; line-height: 10.3px; }
  .letter__date { top: 128px; }
  .letter__recipient { top: 150px; line-height: 11px; }
  .letter__salutation { top: 196px; font-size: 10px; line-height: 13px; }
  .letter__body { top: 222px; text-align: justify; }
  .letter__body p + p { margin-top: 10.3px; }
  .letter__closing { top: 481px; }
  .signature { position: absolute; left: 42px; top: 502px; width: 113px; height: 29px; background: var(--sig-tone); border-radius: 3px; }

  .footer-band { position: absolute; left: 0; right: 0; bottom: 0; height: 12px; display: flex; }
  .footer-band__main { width: 349px; background: var(--navy); }
  .footer-band__gap { width: 4px; }
  .footer-band__side { flex: 1; background: var(--grey-band); }

  .grid { position: absolute; left: 42px; border-collapse: collapse; font-size: 7.5px; table-layout: fixed; }
  .grid th { background: var(--navy); color: #fff; font-weight: 700; text-align: center; border-left: 1px solid #fff; }
  .grid th:first-child { border-left: 0; }
  .grid td { border: 1px solid var(--rule); text-align: center; }
  .bill { top: 136px; width: 383px; }
  .bill th { height: 20px; }
  .bill th:first-child { text-align: left; padding-left: 4px; }
  .bill td { height: 20px; }
  .items { top: 189px; width: 386px; }
  .items th { height: 23px; }
  .items th:first-child { text-align: left; padding-left: 4px; }
  .items td { height: 20.2px; }

  .totals { position: absolute; left: 311px; top: 413px; width: 117px; border-collapse: collapse; font-size: 7.5px; table-layout: fixed; }
  .totals td { border: 1px solid var(--rule); padding-left: 4px; height: 20px; }
  .totals tr.short td { height: 17.5px; }
  .totals .strong { color: var(--navy); font-weight: 700; }

  .terms { position: absolute; left: 42px; top: 446px; font-size: 7.5px; line-height: 12px; }
  .terms__title { font-weight: 700; color: var(--navy); }
  .terms__bank { margin-top: 8px; }
  .thanks { position: absolute; left: 41px; top: 540px; font-size: 8.5px; font-weight: 700; color: var(--navy); }
</style>
</head>
<body>

<section class="sheet sheet--letter">
  <div class="brand">
    <p class="brand__name">The Calder Firm PLC</p>
  </div>
  <div class="contact">
    <p>Maple House Centre Holbrook</p>
    <p>St Andrew, Barbados</p>
    <p class="gap">+44 (0) 7400 555 218</p>
    <p>info@thecalderfirmplc.com</p>
    <p>www.thecalderfirmplc.com</p>
  </div>

  <p class="letter letter__date">December-29-2024</p>
  <div class="letter letter__recipient">
    <p>Arden Works Ltd</p>
    <p>123 Street Name, Suite# 10</p>
    <p>City, State, 120023</p>
  </div>
  <p class="letter letter__salutation">Dear Mr, Daniel</p>
  <div class="letter letter__body">
    <p>Lorem ipsum dolor sit amet, consectetur adipisicing elit, sed do eiusmod tempor incididunt ut labore et dolore magna aliqua. Ut enim ad minim veniam, quis nostrud exercitation ullamco laboris nisi ut aliquip ex ea commodo consequat. Duis aute irure dolor in reprehenderit in voluptate velit esse cillum dolore eu fugiat nulla pariatur.</p>
    <p>Lorem ipsum dolor sit amet, consectetur adipisicing elit, sed do eiusmod tempor incididunt ut labore et dolore magna aliqua. Ut enim ad minim veniam, quis nostrud exercitation ullamco laboris nisi ut aliquip ex ea commodo consequat. Duis aute irure dolor in reprehenderit in voluptate velit esse cillum dolore eu fugiat nulla pariatur.</p>
    <p>Lorem ipsum dolor sit amet, consectetur adipisicing elit, sed do eiusmod tempor incididunt ut labore et dolore magna aliqua. Ut enim ad minim veniam, quis nostrud exercitation ullamco laboris nisi ut aliquip ex ea commodo consequat.</p>
    <p>Excepteur sint occaecat cupidatat non proident, sunt in culpa qui officia deserunt mollit anim id est laborum. re et dolore magnam aliquam quaerat voluptatem.</p>
    <p>Lorem ipsum dolor sit amet, consectetur adipisicing elit, sed do eiusmod tempor incididunt ut labore et dolore magna aliqua. Ut enim ad minim veniam, quis nostrud exercitation ullamco laboris nisi ut aliquip ex ea commodo consequat.</p>
    <p>Excepteur sint occaecat cupidatat non proident, sunt in culpa qui officia deserunt mollit anim id est laborum. re et dolore magnam aliquam quaerat voluptatem.</p>
  </div>
  <p class="letter letter__closing">Regards</p>
  <div class="signature" role="img" aria-label="Handwritten signature of Owen T. Marsh"></div>

  <div class="footer-band"><span class="footer-band__main"></span><span class="footer-band__gap"></span><span class="footer-band__side"></span></div>
</section>

<section class="sheet sheet--invoice">
  <div class="brand">
    <p class="brand__name">The Calder Firm PLC</p>
  </div>
  <h1 class="invoice-title">INVOICE</h1>
  <div class="contact">
    <p>Maple House Centre Holbrook</p>
    <p>St Andrew, Barbados</p>
    <p class="gap">+44 (0) 7400 555 218</p>
    <p>info@thecalderfirmplc.com</p>
    <p>www.thecalderfirmplc.com</p>
  </div>

  <table class="grid bill">
    <colgroup><col style="width:105px"><col style="width:72px"><col style="width:70px"><col style="width:71px"><col style="width:65px"></colgroup>
    <tr><th>Bill To:</th><th>Due Date</th><th>Date Issued</th><th>Invoice Number</th><th>Amount Due</th></tr>
    <tr><td></td><td>10/01/2023</td><td>01/01/2023</td><td>Inv- 0215</td><td>$1528.00</td></tr>
  </table>

  <table class="grid items">
    <colgroup><col style="width:31px"><col style="width:177px"><col style="width:61px"><col style="width:51px"><col style="width:66px"></colgroup>
    <tr><th>SL NO</th><th>DESCRIPTION</th><th>QUANTITY</th><th>RATE</th><th>AMOUNT</th></tr>
    <tr><td></td><td></td><td></td><td></td><td></td></tr>
    <tr><td></td><td></td><td></td><td></td><td></td></tr>
    <tr><td></td><td></td><td></td><td></td><td></td></tr>
    <tr><td></td><td></td><td></td><td></td><td></td></tr>
    <tr><td></td><td></td><td></td><td></td><td></td></tr>
    <tr><td></td><td></td><td></td><td></td><td></td></tr>
    <tr><td></td><td></td><td></td><td></td><td></td></tr>
    <tr><td></td><td></td><td></td><td></td><td></td></tr>
    <tr><td></td><td></td><td></td><td></td><td></td></tr>
    <tr><td></td><td></td><td></td><td></td><td></td></tr>
  </table>

  <table class="totals">
    <colgroup><col style="width:51px"><col style="width:66px"></colgroup>
    <tr><td class="strong">Sub Total</td><td></td></tr>
    <tr><td>Discount</td><td></td></tr>
    <tr><td>Tax</td><td></td></tr>
    <tr class="short"><td>Total</td><td></td></tr>
    <tr class="short"><td class="strong">Total Due</td><td></td></tr>
  </table>

  <div class="terms">
    <p class="terms__title">Terms</p>
    <p>Please pay within 5 working Days using the following bank details:</p>
    <div class="terms__bank">
      <p>Bank Name:</p>
      <p>Account Number:</p>
      <p>Routing Number:</p>
      <p>Account Name:</p>
    </div>
  </div>
  <p class="thanks">Thank you for your Business!</p>

  <div class="footer-band"><span class="footer-band__main"></span><span class="footer-band__gap"></span><span class="footer-band__side"></span></div>
</section>

</body>
</html>
```